Custom Cabinet Shop Needs a website design

Hi,
We need a website for a Custom Cabinet Shop and Cabinet parts manufacturing business.
The business has two sides to it. One side provides custom Kitchens, vanities, entertainment units, offices and what not to homeowners and contractors.
The 2nd side of the business provides built to order cabinet boxes and other parts required to put together a project to other cabinet shops, small contractors looking to install there own cabinets.
Website will need a Gallery to display work.
Color scheme to go well with logo.
current website is www.brindlewoodcustomcabinets.com
being changed to www.brindlewood.ca
Logo Included in attached files.
Tagline "Millwork with Flare"
Mission Statement "Our passion is to deliver inspired cabinetry solutions to suit all your needs, supported by our phenomenal star class customer service"
The website should convey quality and professionalism.
Thank you.
Homeowners/ Contractors
Entertainment
Coded - Design and coding required
1 page

```html
<!DOCTYPE html>
<html lang="en">
<head>
<meta charset="utf-8">
<title>Brindlewood Custom Cabinets</title>
<link href="https://fonts.googleapis.com/css2?family=Open+Sans:wght@400;600;700&family=Montserrat:wght@600&display=swap" rel="stylesheet">
<style>
  :root {
    --orange: #f15f24;
    --dark: #231f20;
    --ink: #222222;
    --grey-bg: #efefef;
    --card-bg: #eeeeee;
    --white: #ffffff;
    --muted: #9a9a9a;
  }
  * { box-sizing: border-box; margin: 0; padding: 0; }
  html, body { width: 1200px; height: 2436px; overflow: hidden; }
  body { position: relative; font-family: "Open Sans", Arial, sans-serif; color: var(--ink); background: var(--white); }
  .abs { position: absolute; }

  /* Header */
  .site-header { left: 0; top: 0; width: 1200px; height: 565px; background: var(--orange); }
  .contact-strip { left: 817px; top: 0; width: 158px; height: 28px; background: var(--dark); display: flex; align-items: center; }
  .contact-phone { color: var(--white); font-size: 13px; font-weight: 700; display: flex; align-items: center; gap: 6px; padding-left: 14px; width: 117px; }
  .contact-pin { width: 41px; height: 28px; background: var(--white); display: flex; align-items: center; justify-content: center; }
  .brand { left: 0; top: 22px; width: 1200px; text-align: center; font-size: 34px; font-weight: 700; color: var(--dark); letter-spacing: 2px; line-height: 44px; }
  .brand-sub { left: 0; top: 66px; width: 1200px; text-align: center; font-size: 10px; font-weight: 700; color: var(--dark); letter-spacing: 5px; }
  .header-rule { left: 224px; top: 102px; width: 751px; height: 2px; background: var(--white); }
  .nav-active-bar { left: 444px; top: 102px; width: 50px; height: 4px; background: var(--dark); }
  .main-nav { left: 224px; top: 111px; width: 751px; display: flex; justify-content: center; gap: 19px; }
  .main-nav a { color: var(--white); text-decoration: none; font-size: 13px; font-weight: 600; letter-spacing: .3px; }
  .main-nav a.is-active { color: var(--dark); }
  .hero { left: 224px; top: 136px; width: 751px; height: 429px; background: linear-gradient(160deg, #cfc7bc 0%, #8a7c6c 35%, #3b2f28 65%, #6b4a32 100%); }
  .hero-caption { left: 677px; top: 325px; width: 298px; height: 37px; background: var(--dark); color: var(--white); font-size: 20px; letter-spacing: 1px; display: flex; align-items: center; justify-content: center; }
  .hero-dots { left: 922px; top: 378px; display: flex; gap: 3px; }
  .hero-dots span { width: 6px; height: 6px; border-radius: 50%; background: var(--white); }
  .hero-dots span.is-current { background: var(--orange); }

  /* Mission */
  .mission { left: 0; top: 565px; width: 1200px; height: 689px; background: var(--grey-bg); }
  .section-title { left: 0; width: 1200px; text-align: center; font-size: 39px; font-weight: 400; color: var(--ink); }
  .section-lead { left: 270px; width: 660px; text-align: center; font-size: 15.5px; line-height: 20px; color: var(--ink); }
  .gallery-label { left: 499px; top: 751px; width: 202px; display: flex; align-items: center; gap: 8px; color: var(--orange); font-size: 11px; letter-spacing: .5px; }
  .gallery-label::before, .gallery-label::after { content: ""; flex: 1; height: 1px; background: var(--orange); }
  .gallery-grid { left: 224px; top: 797px; width: 751px; height: 374px; display: grid; grid-template-columns: repeat(4, 1fr); grid-template-rows: repeat(2, 1fr); gap: 2px; }
  .gallery-tile { position: relative; }
  .tile-heart { position: absolute; right: 10px; top: 10px; }
  .tile-overlay { position: absolute; left: 0; right: 0; bottom: 0; height: 48px; background: rgba(241,95,36,.85); color: var(--white); font-size: 13px; display: flex; align-items: center; justify-content: center; }
  .t1 { background: linear-gradient(160deg, #dfe3d9, #a8906f 60%, #5d4734); }
  .t2 { background: linear-gradient(160deg, #8c8a86, #4b3b32 55%, #a52b2b); }
  .t3 { background: linear-gradient(160deg, #9aa39a, #6f7468 50%, #3a3630); }
  .t4 { background: linear-gradient(160deg, #2a2422, #4a3525 55%, #b8863c); }
  .t5 { background: linear-gradient(160deg, #3a2d2a, #d9cdb9 45%, #5c2a22); }
  .t6 { background: linear-gradient(160deg, #e8e4dc, #b5ab9a 55%, #4b3f36); }
  .t7 { background: linear-gradient(160deg, #eeeeee, #3d2a22 40%, #5a4030); }
  .t8 { background: linear-gradient(160deg, #3a2d2a, #d9cdb9 45%, #5c2a22); }
  .gallery-arrow { top: 977px; }

  /* Services */
  .service-card { width: 314px; height: 489px; top: 1470px; background: var(--card-bg); border: 1px solid #d8d8d8; box-shadow: 0 1px 2px rgba(0,0,0,.08); }
  .card-photo { position: absolute; left: 0; top: 0; width: 100%; height: 214px; }
  .card-photo.kitchen { background: linear-gradient(170deg, #e9e4da, #b9a88e 50%, #3b2a22); }
  .card-photo.entertainment { background: linear-gradient(170deg, #6e4b46, #2a2224 45%, #7a3524); }
  .card-title { position: absolute; left: 61px; top: 250px; font-family: "Montserrat", "Open Sans", sans-serif; font-weight: 600; font-size: 18px; color: var(--orange); }
  .card-list { position: absolute; left: 58px; top: 288px; width: 210px; list-style: none; font-size: 10.5px; line-height: 13px; color: var(--ink); }
  .card-list li { display: flex; gap: 6px; margin-bottom: 11px; }
  .card-list svg { flex: none; margin-top: 1px; }
  .card-button { position: absolute; left: 61px; width: 79px; height: 27px; background: var(--dark); color: var(--white); font-size: 10.5px; display: flex; align-items: center; justify-content: center; }

  /* Footer */
  .site-footer { left: 0; top: 2062px; width: 1200px; height: 374px; background: var(--dark); color: #cfcfcf; }
  .footer-brand { left: 0; top: 2138px; width: 1200px; text-align: center; color: var(--orange); font-size: 20px; font-weight: 700; letter-spacing: 1px; }
  .footer-line { left: 0; width: 1200px; text-align: center; }
  .footer-social { left: 561px; top: 2250px; display: flex; gap: 6px; }
  .footer-social span { width: 16px; height: 16px; border-radius: 50%; border: 1px solid #cfcfcf; }
  .footer-rule { left: 224px; top: 2334px; width: 751px; height: 1px; background: #444; }
  .footer-nav { left: 0; top: 2345px; width: 1200px; display: flex; justify-content: center; gap: 14px; }
  .footer-nav a { color: var(--muted); font-size: 9.5px; text-decoration: none; }
</style>
</head>
<body>

<header class="abs site-header"></header>
<div class="abs contact-strip">
  <span class="contact-phone">
    <svg width="10" height="10" viewBox="0 0 24 24"><path fill="#fff" d="M6.6 10.8a15 15 0 006.6 6.6l2.2-2.2c.3-.3.7-.4 1-.2 1.1.4 2.3.6 3.6.6.6 0 1 .4 1 1V20c0 .6-.4 1-1 1A17 17 0 013 4c0-.6.4-1 1-1h3.5c.6 0 1 .4 1 1 0 1.3.2 2.5.6 3.6.1.3 0 .7-.2 1z"/></svg>
    403-555-0148
  </span>
  <span class="contact-pin">
    <svg width="10" height="13" viewBox="0 0 24 32"><path fill="#231f20" d="M12 0C5.4 0 0 5.4 0 12c0 9 12 20 12 20s12-11 12-20C24 5.4 18.6 0 12 0zm0 17a5 5 0 110-10 5 5 0 010 10z"/></svg>
  </span>
</div>
<div class="abs brand">BRINDLEWOOD</div>
<div class="abs brand-sub">CUSTOM CABINETS</div>
<div class="abs header-rule"></div>
<div class="abs nav-active-bar"></div>
<nav class="abs main-nav">
  <a href="#">HOME</a>
  <a href="#" class="is-active">MISSION</a>
  <a href="#">GALLERY</a>
  <a href="#">SERVICES</a>
  <a href="#">WARRANTY</a>
  <a href="#">CONTACT</a>
</nav>
<div class="abs hero" role="img" aria-label="Photo of an open-plan kitchen with dark wood cabinets, a long granite island with bar stools and pendant lights"></div>
<div class="abs hero-caption">MILLWORK WITH FLARE</div>
<div class="abs hero-dots"><span class="is-current"></span><span></span><span></span><span></span></div>

<section class="abs mission"></section>
<h2 class="abs section-title" style="top:635px;">Mission</h2>
<p class="abs section-lead" style="top:693px;">Our passion is to deliver inspired cabinetry solutions to suit all your needs, supported by our phenomenal star class customer service</p>
<div class="abs gallery-label">GALLERY</div>
<svg class="abs gallery-arrow" style="left:186px;" width="14" height="22" viewBox="0 0 14 22"><path d="M12 2L3 11l9 9" fill="none" stroke="#aaa" stroke-width="3"/></svg>
<svg class="abs gallery-arrow" style="left:999px;" width="14" height="22" viewBox="0 0 14 22"><path d="M2 2l9 9-9 9" fill="none" stroke="#aaa" stroke-width="3"/></svg>
<div class="abs gallery-grid">
  <div class="gallery-tile t1" role="img" aria-label="Photo of a bright dining nook with window seating">
    <svg class="tile-heart" width="18" height="16" viewBox="0 0 24 21"><path fill="#fff" d="M12 21l-1.7-1.6C4.2 13.9 0 10.1 0 5.5A5.5 5.5 0 0112 2.3 5.5 5.5 0 0124 5.5c0 4.6-4.2 8.4-10.3 13.9z"/></svg>
    <div class="tile-overlay">Lorem title text</div>
  </div>
  <div class="gallery-tile t2" role="img" aria-label="Photo of a bathroom vanity beside a soaker tub">
    <svg class="tile-heart" width="18" height="16" viewBox="0 0 24 21"><path fill="#fff" d="M12 21l-1.7-1.6C4.2 13.9 0 10.1 0 5.5A5.5 5.5 0 0112 2.3 5.5 5.5 0 0124 5.5c0 4.6-4.2 8.4-10.3 13.9z"/></svg>
  </div>
  <div class="gallery-tile t3" role="img" aria-label="Photo of a kitchen island with stone front and pendant lights">
    <svg class="tile-heart" width="18" height="16" viewBox="0 0 24 21"><path fill="#fff" d="M12 21l-1.7-1.6C4.2 13.9 0 10.1 0 5.5A5.5 5.5 0 0112 2.3 5.5 5.5 0 0124 5.5c0 4.6-4.2 8.4-10.3 13.9z"/></svg>
  </div>
  <div class="gallery-tile t4" role="img" aria-label="Photo of dark kitchen cabinets with a tiled backsplash">
    <svg class="tile-heart" width="18" height="16" viewBox="0 0 24 21"><path fill="#fff" d="M12 21l-1.7-1.6C4.2 13.9 0 10.1 0 5.5A5.5 5.5 0 0112 2.3 5.5 5.5 0 0124 5.5c0 4.6-4.2 8.4-10.3 13.9z"/></svg>
  </div>
  <div class="gallery-tile t5" role="img" aria-label="Photo of a wet bar with wine rack and cherry cabinets">
    <svg class="tile-heart" width="18" height="16" viewBox="0 0 24 21"><path fill="#fff" d="M12 21l-1.7-1.6C4.2 13.9 0 10.1 0 5.5A5.5 5.5 0 0112 2.3 5.5 5.5 0 0124 5.5c0 4.6-4.2 8.4-10.3 13.9z"/></svg>
  </div>
  <div class="gallery-tile t6" role="img" aria-label="Photo of a white kitchen with island and bar stools">
    <svg class="tile-heart" width="18" height="16" viewBox="0 0 24 21"><path fill="#fff" d="M12 21l-1.7-1.6C4.2 13.9 0 10.1 0 5.5A5.5 5.5 0 0112 2.3 5.5 5.5 0 0124 5.5c0 4.6-4.2 8.4-10.3 13.9z"/></svg>
  </div>
  <div class="gallery-tile t7" role="img" aria-label="Photo of a tall dark wood display cabinet with glass doors"></div>
  <div class="gallery-tile t8" role="img" aria-label="Photo of a wet bar with wine rack and cherry cabinets">
    <svg class="tile-heart" width="18" height="16" viewBox="0 0 24 21"><path fill="#fff" d="M12 21l-1.7-1.6C4.2 13.9 0 10.1 0 5.5A5.5 5.5 0 0112 2.3 5.5 5.5 0 0124 5.5c0 4.6-4.2 8.4-10.3 13.9z"/></svg>
  </div>
</div>

<h2 class="abs section-title" style="top:1313px;">Services</h2>
<p class="abs section-lead" style="top:1381px; left:270px; width:660px;">Lorem ipsum dolor sit amet, consectetur adipisicing elit, sed do eiusmod tempor incididunt ut labore et dolore magna aliqua. Ut enim ad minim veniam</p>

<article class="abs service-card" style="left:271px;">
  <div class="card-photo kitchen" role="img" aria-label="Photo of a custom kitchen with a dark island and white upper cabinets"></div>
  <h3 class="card-title">One Side Provides</h3>
  <ul class="card-list">
    <li><svg width="10" height="10" viewBox="0 0 10 10"><path d="M1 5l3 3 5-6" fill="none" stroke="#222" stroke-width="1.3"/></svg>Lorem ipsum dolor sit amet</li>
    <li><svg width="10" height="10" viewBox="0 0 10 10"><path d="M1 5l3 3 5-6" fill="none" stroke="#222" stroke-width="1.3"/></svg>Consectetur adipisicing elit sed</li>
    <li><svg width="10" height="10" viewBox="0 0 10 10"><path d="M1 5l3 3 5-6" fill="none" stroke="#222" stroke-width="1.3"/></svg>tempor incididunt ut labore</li>
    <li><svg width="10" height="10" viewBox="0 0 10 10"><path d="M1 5l3 3 5-6" fill="none" stroke="#222" stroke-width="1.3"/></svg>sed do eiusmod tempor incididunt labore et</li>
  </ul>
  <div class="card-button" style="top:406px;">Click Here</div>
</article>

<article class="abs service-card" style="left:624px;">
  <div class="card-photo entertainment" role="img" aria-label="Photo of a cherry wood entertainment unit with a wall-mounted TV and tall speakers"></div>
  <h3 class="card-title">Second Side Provides</h3>
  <ul class="card-list">
    <li><svg width="10" height="10" viewBox="0 0 10 10"><path d="M1 5l3 3 5-6" fill="none" stroke="#222" stroke-width="1.3"/></svg>Lorem ipsum dolor sit amet</li>
    <li><svg width="10" height="10" viewBox="0 0 10 10"><path d="M1 5l3 3 5-6" fill="none" stroke="#222" stroke-width="1.3"/></svg>Consectetur adipisicing elit sed</li>
    <li><svg width="10" height="10" viewBox="0 0 10 10"><path d="M1 5l3 3 5-6" fill="none" stroke="#222" stroke-width="1.3"/></svg>tempor incididunt ut labore</li>
    <li><svg width="10" height="10" viewBox="0 0 10 10"><path d="M1 5l3 3 5-6" fill="none" stroke="#222" stroke-width="1.3"/></svg>sed do eiusmod tempor incididunt labore et</li>
  </ul>
  <div class="card-button" style="top:401px;">Click Here</div>
</article>

<footer class="abs site-footer"></footer>
<div class="abs footer-brand">BRINDLEWOOD</div>
<div class="abs footer-line" style="top:2204px; font-size:10px;">1207 Maple Bend Road Alder Valley, Alberta, T4X 2J</div>
<div class="abs footer-line" style="top:2222px; font-size:12.5px;">Tel: 403-555-0148 or 403-555-0193</div>
<div class="abs footer-social"><span></span><span></span><span></span><span></span></div>
<div class="abs footer-line" style="top:2299px; font-size:10px;">© 2015</div>
<div class="abs footer-rule"></div>
<nav class="abs footer-nav">
  <a href="#">HOME</a><a href="#">ABOUT</a><a href="#">GALLERY</a><a href="#">SERVICES</a><a href="#">WARRANTY</a><a href="#">CONTACT</a>
</nav>

</body>
</html>
```